Create and Design Brand Guidelines for IT Company

Brindle Networks Logo and Branding Objective
Brindle Networks is upgrading its brand assets, marketing collateral and website. The company is seeking a graphic designer's expertise to develop a style guide that creates brand consistency and communicates to internal and external stakeholders how to position the Brindle Networks brand when assigned tasks relating to the brand. The brand style guide should have information about the logo and clear usage guidelines, a recommended font to use, a colour profile including HEX code, RGB, CMYK, Pantone codes, and iconography recommendations. Details about the company tone, voice and photography usage will be added by Brindle Networks.
Look and feel
Each slider illustrates characteristics of the customer's brand and the style your logo design should communicate.

```html
<!DOCTYPE html>
<html lang="en">
<head>
<meta charset="utf-8">
<title>Brindle Networks Brand Guidelines</title>
<link rel="stylesheet" href="https://fonts.googleapis.com/css2?family=Montserrat:wght@400;500;600;700&display=swap">
<style>
:root{
  --brand-green:#93c854;
  --brand-gray:#636466;
  --ink:#3a3a3c;
  --panel:#f1f1f1;
  --white:#ffffff;
  --mock-dark:#4a4d50;
  --mock-light:#e6e8e4;
}
*{margin:0;padding:0;box-sizing:border-box}
html,body{width:1200px;height:2204px;overflow:hidden;background:var(--white)}
body{font-family:"Montserrat",Arial,sans-serif;color:var(--ink);position:relative}
.abs{position:absolute}
.hero-wordmark{left:0;width:1200px;top:190px;text-align:center;font-size:78px;font-weight:600;color:var(--brand-green);letter-spacing:2px}
.intro-band{left:0;top:440px;width:1200px;height:540px;background:var(--brand-green)}
.intro-wordmark{left:80px;top:500px;font-size:48px;font-weight:600;color:var(--white)}
.intro-tagline{left:80px;top:600px;font-size:19px;font-weight:700;color:var(--white);letter-spacing:.5px}
.intro-copy{left:80px;top:640px;width:430px;font-size:11.5px;line-height:1.55;color:var(--white)}
.intro-copy p{margin-bottom:12px}
.brochure-mockup{left:560px;top:380px;width:620px;height:700px;background:linear-gradient(160deg,var(--mock-dark) 0%,var(--mock-dark) 45%,var(--mock-light) 46%,#f7f7f5 100%);border-radius:4px;box-shadow:0 20px 40px rgba(0,0,0,.2)}
.font-panel{left:80px;top:1050px;width:720px;height:130px;background:var(--panel)}
.font-name{left:110px;top:1075px;font-size:38px;font-weight:700;color:var(--brand-green)}
.font-sub{left:110px;top:1128px;font-size:20px;color:var(--brand-gray)}
.font-aa{left:660px;top:1070px;font-size:72px;font-weight:600;color:#dcdcdc}
.type-label{left:80px;font-size:24px;letter-spacing:6px;color:var(--ink)}
.type-label.bold{font-weight:700}
.type-glyphs{left:380px;width:420px;font-size:24px;letter-spacing:9px;line-height:1.6}
.type-glyphs.bold{font-weight:700}
.swatch{left:840px;width:320px;height:200px;border-radius:10px}
.swatch span{position:absolute;left:28px;bottom:24px;font-size:22px;font-weight:600;color:var(--white)}
.swatch-green{top:1050px;background:var(--brand-green)}
.swatch-gray{top:1360px;background:var(--brand-gray)}
.tint-row{left:840px;width:320px;height:14px;display:flex;gap:8px}
.tint-row i{flex:1;border-radius:3px}
.recommend{left:80px;top:1620px;width:700px;font-size:22px;line-height:1.45;color:var(--ink)}
.impl-band{left:0;top:1740px;width:1200px;height:370px;background:var(--brand-green)}
.cards-mockup{left:20px;top:1830px;width:420px;height:320px;background:linear-gradient(135deg,#ffffff 0%,#e4e6e2 60%,#c9ccc6 100%);border-radius:6px;box-shadow:0 14px 30px rgba(0,0,0,.18)}
.impl-title{left:560px;top:1880px;font-size:30px;line-height:1.1;color:var(--white)}
.impl-copy{left:560px;top:1960px;width:270px;font-size:18px;line-height:1.4;color:var(--white)}
.letterhead-mockup{left:860px;top:1620px;width:320px;height:560px;background:linear-gradient(180deg,#ffffff 0%,#f2f2f0 100%);box-shadow:0 16px 34px rgba(0,0,0,.2)}
</style>
</head>
<body>
  <div class="abs hero-wordmark">Brindle Networks</div>

  <div class="abs intro-band"></div>
  <div class="abs intro-wordmark">Brindle Networks</div>
  <div class="abs intro-tagline">IT SUPPORT FOR THE AMBITIOUS BUSINESS</div>
  <div class="abs intro-copy">
    <p>Founded in 2010, Brindle Networks delivers dependable IT support, managed networks and cloud services to growing firms that expect reliable technology every single working day.</p>
    <p>Our engineers partner with each client, planning secure systems, proactive monitoring and fast helpdesk response so teams can focus on their ambitious goals.</p>
    <p>These guidelines explain how to present our name, colours and type consistently across print, digital and every customer touchpoint.</p>
  </div>
  <div class="abs brochure-mockup" role="img" aria-label="Brand guidelines brochure held open, cover showing a person at a laptop"></div>

  <div class="abs font-panel"></div>
  <div class="abs font-name">Montserrat Bold</div>
  <div class="abs font-sub">Montserrat Regular</div>
  <div class="abs font-aa">Aa</div>

  <div class="abs type-label bold" style="top:1220px">BOLD</div>
  <div class="abs type-glyphs bold" style="top:1210px">ABCDEFGHIJKLM NOPQRSTUVWXYZ</div>
  <div class="abs type-label" style="top:1370px">REGULAR</div>
  <div class="abs type-glyphs" style="top:1360px">abcdefghijklm nopqrstuvwxyz</div>
  <div class="abs type-label" style="top:1510px">NUMERIC</div>
  <div class="abs type-glyphs" style="top:1502px">1234567890</div>

  <div class="abs swatch swatch-green"><span>#93C854</span></div>
  <div class="abs tint-row" style="top:1270px"><i style="background:#b4d98a"></i><i style="background:#c9e4a8"></i><i style="background:#ddefc6"></i><i style="background:#eef7e3"></i></div>
  <div class="abs swatch swatch-gray"><span>#636466</span></div>

  <div class="abs recommend">Recommend use Fontstyle and Color Tone Brindle Networks brand when assigned tasks relating to the brand.</div>

  <div class="abs impl-band"></div>
  <div class="abs cards-mockup" role="img" aria-label="Stack of fanned business cards"></div>
  <div class="abs impl-title">LOGO<br>IMPLEMENTATION</div>
  <div class="abs impl-copy">Use logo Brindle Networks brand when assigned tasks relating to the brand.</div>
  <div class="abs letterhead-mockup" role="img" aria-label="Letterhead sheet with logo and body text"></div>
</body>
</html>
```